Vita Shield Prime is a new Chinese herbal medicine nutritional supplement.

I need a label design for my Dr Penwick Rx Chinese herbal supplement line .
I am launching a new super powerful immune booster
Vita Shield Prime.
The FRONT label 3 in. x 4 in. Black mylar bag will have 30 capsules
The Back label will be the size 3 inches x 3 inches will send information
Target Market(s)
Females 25 to 80 who buy nutritional supplements for themselves and their families.
Industry/Entity Type
Medicine
Font styles to use
Decorative
Colors
Designer to choose colors to be used in the design.
Requirements
Must have
- Dr Penwick Rx the name of the company. A wax seal with the an imprint of the name stamp letters on wax .. examples will be provided below.. an image of name stamp inside wax seal. Product name is Vita Shield Prime. Must use traditional Chinese colors. COLORS BELOW IN SAVED IMAGES.. GOLD, BLOOD RED, DARK PURPLE. description of product... Powerful Immune Booster.. a clear and easy to read label. ALL SO BACK LABEL 3 INCHES X 3 INCHES USING ONLY TWO COLORS.. BASIC PRODUCT LABEL OF INGREDIENTS, SUGGESTED USE, PRODUCT INFO, AND WARNINGS. IMAGES FILE 3 IS TO BE USED IN WAX SEAL.USE ONLY EXAMPLE COLORS BELOW IN IMAGES
Nice to have
- I like royal colors of ancient China, which happen to be strong psychological colors for marketing. A Gold wax with my name stamp in red or something like that. "Ancient Chinese secret for modern health".
Should not have

```html
<!DOCTYPE html>
<html lang="en">
<head>
<meta charset="utf-8">
<title>Dr Penwick Rx – Vita Shield Prime Label</title>
<link rel="stylesheet" href="https://fonts.googleapis.com/css2?family=Montserrat:wght@600;800&family=UnifrakturCook:wght@700&family=Ma+Shan+Zheng&display=swap">
<style>
  :root {
    --page: #ececec;
    --frame-dark: #4a3a33;
    --frame-tan: #c89a7a;
    --blood-red: #a3262e;
    --royal-purple: #3b2468;
    --banner-tan: #efd7bd;
    --band-tan: #d9ae7f;
    --ink-brown: #4a3b33;
    --gold: #f2c94c;
    --gold-deep: #b8860b;
    --dragon-red: #b3322e;
  }
  html, body {
    margin: 0;
    width: 1200px;
    height: 1200px;
    overflow: hidden;
    background: var(--page);
  }
  .label {
    position: absolute;
    left: 215px;
    top: 50px;
    width: 770px;
    height: 1100px;
    display: block;
  }
  .brand-name {
    font-family: "Montserrat", sans-serif;
    font-weight: 800;
    font-size: 72px;
    fill: var(--ink-brown);
    letter-spacing: 1px;
  }
  .product-name {
    font-family: "Montserrat", sans-serif;
    font-weight: 600;
    font-size: 38px;
    fill: var(--ink-brown);
    stroke: var(--banner-tan);
    stroke-width: 1px;
    letter-spacing: 2px;
  }
  .product-name--on-purple { fill: var(--banner-tan); stroke: var(--ink-brown); }
  .category {
    font-family: "UnifrakturCook", serif;
    font-weight: 700;
    font-size: 52px;
    fill: var(--gold);
    stroke: #3a2a12;
    stroke-width: 1.5px;
    paint-order: stroke;
  }
  .count {
    font-family: "Montserrat", sans-serif;
    font-weight: 800;
    font-size: 18px;
    fill: var(--gold);
    letter-spacing: 1px;
  }
  .motto {
    font-family: "Ma Shan Zheng", cursive;
    font-size: 92px;
    fill: var(--ink-brown);
  }
  .rule { stroke: var(--frame-tan); stroke-width: 3; }
</style>
</head>
<body>
<svg class="label" viewBox="0 0 720 1030" xmlns="http://www.w3.org/2000/svg">
  <defs>
    <radialGradient id="dragon-tone" cx="50%" cy="45%" r="60%">
      <stop offset="0" stop-color="#c2403a"/>
      <stop offset="1" stop-color="#8e2530"/>
    </radialGradient>
    <radialGradient id="seal-tone" cx="40%" cy="35%" r="65%">
      <stop offset="0" stop-color="#ffe27a"/>
      <stop offset="0.6" stop-color="#e0a82a"/>
      <stop offset="1" stop-color="#9a6a10"/>
    </radialGradient>
    <path id="brand-arc" d="M110 180 Q360 70 610 180"/>
  </defs>

  <!-- outer frame -->
  <rect class="frame" x="0" y="0" width="720" height="1030" fill="var(--frame-dark)"/>
  <rect x="6" y="6" width="708" height="1018" fill="none" stroke="var(--frame-tan)" stroke-width="4"/>
  <rect x="26" y="22" width="668" height="986" fill="var(--frame-tan)"/>
  <rect x="32" y="28" width="656" height="974" fill="var(--royal-purple)"/>

  <!-- top red band -->
  <path d="M32 28 H688 V125 Q360 10 32 125 Z" fill="var(--blood-red)"/>

  <!-- dragon artwork area -->
  <g role="img" aria-label="Red Chinese dragon illustration coiling down the label">
    <path d="M230 250 Q330 190 470 230 Q560 300 520 420 Q600 520 560 620 Q640 700 580 820 Q420 850 300 830 Q220 740 250 640 Q120 560 170 450 Q90 380 180 300 Z"
          fill="url(#dragon-tone)" opacity="0.9"/>
  </g>

  <!-- arched banner -->
  <path d="M35 122 Q360 30 686 122 L686 220 Q360 120 35 225 Z" fill="var(--banner-tan)" stroke="var(--ink-brown)" stroke-width="3"/>
  <text class="brand-name" text-anchor="middle"><textPath href="#brand-arc" startOffset="50%">DR PENWICK RX</textPath></text>
  <text class="product-name" x="360" y="208" text-anchor="middle">VITA SHIELD</text>
  <text class="product-name product-name--on-purple" x="360" y="246" text-anchor="middle">PRIME</text>

  <!-- category line -->
  <text class="category" x="372" y="458" text-anchor="middle">Traditional Chinese</text>
  <text class="category" x="372" y="508" text-anchor="middle">Herbal Medicine</text>

  <!-- wax seal -->
  <g role="img" aria-label="Gold wax seal stamped with the Dr Penwick Rx name">
    <circle cx="370" cy="625" r="80" fill="url(#seal-tone)"/>
    <circle cx="370" cy="625" r="58" fill="none" stroke="#9a6a10" stroke-width="3"/>
  </g>

  <!-- speed rules -->
  <line class="rule" x1="40" y1="742" x2="130" y2="742"/>
  <line class="rule" x1="40" y1="755" x2="145" y2="755"/>
  <line class="rule" x1="40" y1="768" x2="160" y2="768"/>
  <line class="rule" x1="40" y1="781" x2="175" y2="781"/>
  <line class="rule" x1="40" y1="794" x2="210" y2="794"/>
  <line class="rule" x1="40" y1="807" x2="260" y2="807"/>
  <line class="rule" x1="40" y1="820" x2="280" y2="820"/>

  <text class="count" x="362" y="832" text-anchor="middle">30 CAPSULES</text>

  <!-- bottom motto band -->
  <rect x="32" y="842" width="656" height="6" fill="var(--ink-brown)"/>
  <rect x="32" y="848" width="656" height="135" fill="var(--band-tan)"/>
  <line x1="36" y1="860" x2="684" y2="860" stroke="var(--ink-brown)" stroke-width="2"/>
  <line x1="36" y1="962" x2="684" y2="962" stroke="var(--ink-brown)" stroke-width="2"/>
  <text class="motto" x="210" y="948" text-anchor="middle">健 康</text>
  <text class="motto" x="515" y="948" text-anchor="middle">活 力</text>
  <rect x="32" y="983" width="656" height="8" fill="var(--blood-red)"/>
</svg>
</body>
</html>
```